Heater product information sheets

I need the two product information sheets organized and laid out in a clean, easy to read attractive manner. These sheets are to advertise propane heaters for outdoor use and for wholesale to propane distributors, restaurants and homeowners that need to have propane heat as the winter ends and spring begins. They will be used for chilly evenings when people want to be outside eating, drinking and being social.
Updates

Low design quality

Target Market(s)

Restaurants, hospitality industry, special events, party rental companies, home owners with backyards

Font styles to use
Sans Serif

Requirements
Must have
• My logo in the document instead of r. Kolby and company
Nice to have
• I would like to see Fire illustrated coming up the heaters and on the round glass, show it up the middle of the glass tube propane heater.

```html
<!DOCTYPE html>
<html lang="en">
<head>
<meta charset="utf-8">
<title>Glass Tube Propane Heaters – Product Sheet</title>
<link rel="stylesheet" href="https://fonts.googleapis.com/css2?family=Abril+Fatface&family=Fira+Sans+Condensed:wght@400;500;600;700&family=Josefin+Sans:wght@400;600&display=swap">
<style>
  :root{
    --backdrop:#e6e6e6;
    --paper:#ffffff;
    --orange:#d67d25;
    --yellow:#f9c75f;
    --ink:#2a2a2a;
    --steel-light:#c9c9c9;
    --steel-dark:#1c1c1c;
  }
  *{box-sizing:border-box;margin:0;padding:0}
  html,body{width:1200px;height:960px;overflow:hidden;background:var(--backdrop)}
  .sheet{
    position:absolute;left:240px;top:14px;width:720px;height:932px;
    background:var(--paper);overflow:hidden;
    box-shadow:0 6px 24px rgba(0,0,0,.15);
    font-family:"Fira Sans Condensed",sans-serif;color:var(--ink);
  }
  .waves{position:absolute;inset:0;width:720px;height:932px}
  .product-photo{
    position:absolute;left:540px;top:60px;width:130px;height:410px;
    border-radius:60px 60px 16px 16px;
    background:linear-gradient(to bottom,var(--steel-light) 0%,#e9e9e9 55%,var(--steel-dark) 62%,var(--steel-dark) 100%);
  }
  .headline{
    position:absolute;left:120px;top:96px;
    font-family:"Abril Fatface",serif;color:var(--orange);
    font-size:80px;line-height:76px;letter-spacing:-1px;
  }
  .headline span{display:block}
  .headline span:nth-child(2){padding-left:4px}
  .headline span:nth-child(3){padding-left:10px}
  .headline span:nth-child(4){padding-left:16px}
  .uses{
    position:absolute;left:138px;top:430px;list-style:none;
    font-weight:700;font-size:15px;text-transform:uppercase;line-height:24px;letter-spacing:.2px;
  }
  .uses li::before,.specs li::before,.note li::before{content:"• "}
  .details{
    position:absolute;left:420px;top:568px;width:280px;bottom:16px;padding-left:18px;
    border-left:1.5px solid var(--ink);
  }
  .details::before{
    content:"";position:absolute;left:-4px;top:-5px;width:7px;height:7px;border-radius:50%;background:var(--ink);
  }
  .tag{
    display:inline-block;background:var(--orange);color:#fff;
    font-weight:700;font-size:13.5px;text-transform:uppercase;
    padding:2px 80px 1px 4px;margin-bottom:3px;
  }
  .specs{list-style:none;font-size:12.5px;line-height:15.5px;margin-bottom:7px}
  .specs li{padding-left:9px;text-indent:-9px}
  .note{
    position:absolute;left:108px;top:726px;
    font-family:"Josefin Sans",sans-serif;font-size:14px;line-height:20px;
  }
  .note ul{list-style:none}
  .contact{position:absolute;left:112px;top:808px;font-family:"Josefin Sans",sans-serif}
  .contact-lead{font-size:13px;letter-spacing:3px;font-style:italic;margin-bottom:3px}
  .company{
    display:inline-block;background:var(--orange);color:#fff;
    font-family:"Fira Sans Condensed",sans-serif;font-weight:700;font-size:22px;
    text-transform:uppercase;padding:2px 10px 0 8px;margin-bottom:5px;
  }
  .contact-line{display:flex;align-items:center;gap:9px;font-size:15px;line-height:20px}
  .contact-line svg{width:14px;height:14px;flex:none}
</style>
</head>
<body>
<main class="sheet">
  <svg class="waves" viewBox="0 0 720 932" aria-hidden="true">
    <path fill="var(--orange)" d="M0,540 C60,640 160,700 280,660 C400,620 460,470 580,460 C640,455 690,490 720,520 L720,932 L0,932 Z"/>
    <path fill="var(--yellow)" d="M0,575 C60,675 170,722 290,690 C410,655 470,500 585,495 C645,492 690,522 720,548 L720,932 L0,932 Z"/>
  </svg>

  <div class="product-photo" role="img" aria-label="Photo of a glass tube propane patio heater with steel reflector cap and black base"></div>

  <h1 class="headline"><span>Glass</span><span>Tube</span><span>Propane</span><span>Heaters</span></h1>

  <ul class="uses">
    <li>Rentals for live events</li>
    <li>Rentals for restaurants &amp; catering halls</li>
    <li>Purchase for your home or business</li>
  </ul>

  <section class="details">
    <div class="tag">Specifications</div>
    <ul class="specs">
      <li>Powerful 48,000 BTU</li>
      <li>Black Powder Coated Finish</li>
      <li>Uses 20 lbs. Propane Tank</li>
      <li>CE, GS, AGA, CSA, with ETL certificate and ROHS approved.</li>
    </ul>
    <div class="tag">Additional Details</div>
    <ul class="specs">
      <li>Commercial Quality</li>
      <li>For Outdoor Use Only</li>
      <li>Conforms to ANSI STD Z83.26-2014 Certified to CSA STD 2.37-2014 Gas-fired outdoor infrared patio heaters</li>
      <li>Safety Auto Shut Off Switch</li>
      <li>Thermostatic Control</li>
      <li>Base Diameter 17" - Anti-Tip Design</li>
      <li>Standard Wheels - Tilt &amp; Move</li>
      <li>Run time: 8-10 hours with standard 20 lbs. Propane tank</li>
      <li>96" Tall</li>
      <li>Heating Area: 200 sq. ft</li>
    </ul>
  </section>

  <section class="note">
    <p>NOTE</p>
    <ul>
      <li>Price: Starting at $250 each</li>
      <li>Assembly &amp; Delivery available upon request</li>
      <li>Discounts for large quantity orders</li>
    </ul>
  </section>

  <section class="contact">
    <p class="contact-lead">To Rent or Purchase:</p>
    <div class="company">R. Kolby &amp; Company</div>
    <p class="contact-line">
      <svg viewBox="0 0 14 14" aria-hidden="true"><circle cx="7" cy="7" r="7" fill="var(--orange)"/><path d="M4.5 3.5l1.5 1.6-.8 1a5 5 0 0 0 2.7 2.7l1-.8 1.6 1.5-.9 1.1C6.5 10.3 3.7 7.5 3.4 4.4z" fill="#fff"/></svg>
      555-014-2290
    </p>
    <p class="contact-line">
      <svg viewBox="0 0 14 14" aria-hidden="true"><circle cx="7" cy="7" r="7" fill="var(--orange)"/><rect x="3.5" y="4.5" width="7" height="5" fill="#fff"/><path d="M3.5 4.5L7 7.3l3.5-2.8" stroke="var(--orange)" stroke-width=".9" fill="none"/></svg>
      Mara@kolbyrentals.com
    </p>
    <p class="contact-line">
      <svg viewBox="0 0 14 14" aria-hidden="true"><circle cx="7" cy="7" r="7" fill="var(--orange)"/><path d="M7 11.2S4.3 8.2 4.3 6.1a2.7 2.7 0 0 1 5.4 0c0 2.1-2.7 5.1-2.7 5.1z" fill="#fff"/><circle cx="7" cy="6" r="1" fill="var(--orange)"/></svg>
      42 Orchard Lane Millbrook, NJ 07999
    </p>
  </section>
</main>
</body>
</html>
```